QUORVIX - Sydney Based Technology Consultancy -Logo & Business Card design

Who are we?
-
Quorvix is an emerging and advanced technology consulting and professional services business based in Sydney, Australia. Quorvix specialising in increasing value to organisations through the effective use of current and emerging technologies, ensuring that technology is a sustainable catalyst to attaining stated business goals.

We pride ourselves in challenging the norm.

What do we want?
-
We are looking to update our "Brand" we already have a simple “home grown” logo and we are now looking for a new one, once we have this updated logo and businesses look and feel though the business card design we will refresh our website with the new logo and design thus updating the Companies overall look at feel.

Our current site is www.quorvix-example.net.au is a very basic wordpress site and we will be updating it once we have the new logo and designs done

Our initial thoughts on the new Quorvix identity are
• Logo Concept
- One of the key things is obviously the 8
- I was thinking that a logo that had 8 as the core of the logo would be cool,
- Almost like having a “ring” or hoop that is twisted to form an 8 with different services scribed on the inside.
- So we would have a Large 8 and the inside would have ring each service or section engraved.

• Brand / web Feel
- Simple
- Professional
- Innovative
- Clear
- Destination
- Unique
- Impartial
- Safe
- Leading edge
- Familiar

- Emerging technologies
- White and ice / glacier blue
- The familiar feel of the Brindle web site
- Embedded specialist Video clips

• Portfolio of Services
- Quorvix – A smart place for Smart people
- Quorvix – we provide the process to take ideas from awareness to reality
- Focus should be on the brand quality consistent clear local knowledge with regional, national, theatre and global presence

Access to Specialists
- Emerging technologies
- Sustainability
- Collaboration
- Data centre
- Virtualisation

• Adjacent ideas under the one Brand
- Tembrosk – Enable Business Collaboration
- Plinsk – Infrastructure Virtualisation
- morvo - smart people and processes
- skandel - Emerging technologies
- brunhavel - business to technology integration
- tolpin - Smart Infrastructure
- yusk – Connected communities
- dwol - sustainability

Target Market(s)

Australia, New Zealand and Asia pacific organisations that are typically English speaking.
Markets
- IT & Technology partners
- Banking and Finance
- Health

Industry/Entity Type

Business

Requirements
Must have
• Logo
Business cards
Colour pallette
3D Logo
Nice to have
• Style guide
Designer who can also assist with new Wordpress design
Should not have
• we don't want cheap looking, overtly flashy or gimmicky logo.

```html
<!DOCTYPE html>
<html lang="en">
<head>
<meta charset="utf-8">
<title>Quorvix – Business Card</title>
<link rel="stylesheet" href="https://fonts.googleapis.com/css2?family=Roboto+Slab:wght@900&family=Jost:wght@400;500&display=swap">
<style>
  :root {
    --stage: #ecebe8;
    --glacier: #00b9ef;
    --paper: #ffffff;
    --ink: #6b6b6b;
    --punch: #5a3a22;
    --shadow: rgba(0, 0, 0, 0.28);
  }
  * { box-sizing: border-box; margin: 0; padding: 0; }
  html, body {
    width: 1200px;
    height: 1141px;
    overflow: hidden;
    background: var(--stage);
  }
  .canvas {
    position: relative;
    width: 1200px;
    height: 1141px;
  }
  .card {
    position: absolute;
    width: 750px;
    height: 430px;
    box-shadow: 6px 8px 18px var(--shadow);
  }
  .card--front {
    left: 70px;
    top: 57px;
    background: var(--glacier);
    display: flex;
    align-items: center;
    justify-content: center;
  }
  .brand-name {
    font-family: "Roboto Slab", serif;
    font-weight: 900;
    font-size: 108px;
    line-height: 1;
    color: var(--paper);
    letter-spacing: 0;
  }
  .card--back {
    left: 387px;
    top: 554px;
    background: var(--paper);
  }
  .brand-mark {
    position: absolute;
    left: 122px;
    top: 137px;
    width: 156px;
    height: 156px;
  }
  .contact {
    position: absolute;
    left: 376px;
    top: 98px;
    font-family: "Jost", sans-serif;
    font-size: 16px;
    line-height: 20px;
    color: var(--ink);
  }
  .contact__name {
    font-size: 21px;
    font-weight: 500;
    color: var(--glacier);
    line-height: 24px;
  }
  .contact__group { margin-top: 22px; }
</style>
</head>
<body>
<main class="canvas">
  <section class="card card--front" aria-label="Business card front">
    <h1 class="brand-name">Quorvix</h1>
  </section>

  <section class="card card--back" aria-label="Business card back">
    <svg class="brand-mark" viewBox="0 0 156 156" aria-hidden="true">
      <circle cx="78" cy="78" r="78" fill="var(--punch)"/>
    </svg>
    <div class="contact">
      <p class="contact__name">Name Lastname</p>
      <p class="contact__role">CEO</p>
      <div class="contact__group">
        <p>name@quorvix-example.com</p>
        <p>www.quorvix-example.com</p>
      </div>
      <div class="contact__group">
        <p>1 street</p>
        <p>town</p>
        <p>code</p>
      </div>
      <div class="contact__group">
        <p>+27 82 555 0142</p>
      </div>
    </div>
  </section>
</main>
</body>
</html>
```